For Lease Sign to Attract National Retail Tenants

Attached is a logo design that was created by Pixel Harbor. I will like to develop a leasing sign that is 4 foot wide by 4 foot high or 4 feet wide and 6 feet high. I would like the sign to have a black background and use the colors that are in the logo. These will be signs that are placed in front of shopping centers and are often read by passing motorist so the sign must be simple, clean, very easy to read, distinctive, and have as few words as possible. It would be good if small amounts of bright green can be added as a boarder or ????? The text should be FOR LEASE, 555-283-7716, Wade Hollins. I will want to also design cards and letter head around the same theme.

Target Market(s)

National retail tenants wanting to lease space in my shopping centers

Industry/Entity Type

Real Estate Development

Contact Information for Business Card

Tern Holdings KR, LLC Wade Hollins President & CEO 4127 Orvell Ave. Suite 308 La Jolla, CA 92037 555-283-7716 wadehollins@mailvexa.example

```html
<!DOCTYPE html>
<html lang="en">
<head>
<meta charset="utf-8">
<title>Tern Holdings KR – Letterhead &amp; Business Card</title>
<link rel="stylesheet" href="https://fonts.googleapis.com/css2?family=Open+Sans:wght@400;600&family=Montserrat:wght@700&display=swap">
<style>
  :root {
    --backdrop: #66676c;
    --paper: #ffffff;
    --brand-red: #ee2a35;
    --charcoal: #333333;
    --ink: #222222;
    --footer-ink: #ffffff;
  }
  * { box-sizing: border-box; margin: 0; padding: 0; }
  html, body { width: 1200px; height: 1200px; overflow: hidden; }
  body { background: var(--backdrop); position: relative; font-family: "Open Sans", sans-serif; color: var(--ink); }

  /* Letterhead */
  .letterhead { position: absolute; left: 270px; top: 128px; width: 668px; height: 944px; background: var(--paper); }
  .letterhead__topbar { position: absolute; left: 0; top: 0; width: 100%; height: 10px; background: var(--brand-red); }
  .letterhead__tab { position: absolute; left: 447px; top: 10px; width: 109px; height: 10px; background: var(--brand-red);
    clip-path: polygon(0 0, 100% 0, 93% 100%, 7% 100%); }
  .brand-name { font-family: "Open Sans", sans-serif; font-weight: 600; color: var(--brand-red); white-space: nowrap; display: flex; align-items: center; gap: 8px; }
  .brand-name__mark { display: inline-block; background: var(--brand-red); }
  .letterhead__brand { position: absolute; right: 84px; top: 90px; font-size: 19px; }
  .letterhead__brand .brand-name__mark { width: 10px; height: 10px; }
  .letterhead__footer { position: absolute; left: 0; bottom: 0; width: 100%; height: 56px; background: var(--charcoal); }
  .letterhead__notch { position: absolute; left: 442px; top: 0; width: 120px; height: 18px; background: var(--paper);
    clip-path: polygon(0 0, 100% 0, 88% 100%, 12% 100%); }
  .letterhead__contacts { position: absolute; left: 0; right: 0; top: 26px; display: flex; justify-content: center; gap: 22px;
    font-size: 9px; color: var(--footer-ink); padding-left: 40px; }
  .contact-item { display: flex; align-items: center; gap: 8px; white-space: nowrap; }
  .contact-item svg { width: 9px; height: 9px; fill: currentColor; flex: none; }

  /* Business card */
  .business-card { position: absolute; left: 220px; top: 621px; width: 283px; height: 161px; background: var(--paper); overflow: hidden; }
  .business-card__topbar { position: absolute; left: 0; top: 0; width: 100%; height: 6px; background: var(--brand-red); }
  .business-card__panel { position: absolute; left: 0; top: 6px; width: 100%; height: 99px; background: var(--charcoal); }
  .business-card__tab { position: absolute; left: 138px; top: 6px; width: 112px; height: 10px; background: var(--brand-red);
    clip-path: polygon(0 0, 100% 0, 92% 100%, 8% 100%); }
  .business-card__brand { position: absolute; right: 30px; top: 62px; font-size: 14px; }
  .business-card__brand .brand-name__mark { width: 7px; height: 7px; }
  .business-card__name { position: absolute; left: 136px; top: 99px; width: 116px; height: 24px; background: var(--brand-red);
    clip-path: polygon(0 0, 100% 0, 90% 100%, 10% 100%); color: #fff; font-family: "Montserrat", sans-serif; font-weight: 700;
    font-size: 11px; display: flex; align-items: center; justify-content: center; }
  .business-card__details { position: absolute; font-size: 7px; line-height: 1.4; color: var(--ink); }
  .business-card__details .contact-item { gap: 9px; align-items: flex-start; margin-bottom: 5px; }
  .business-card__details svg { width: 7px; height: 7px; margin-top: 1px; }
  .details--left { left: 22px; top: 118px; }
  .details--right { left: 150px; top: 130px; }
</style>
</head>
<body>

<section class="letterhead">
  <div class="letterhead__topbar"></div>
  <div class="letterhead__tab"></div>
  <div class="letterhead__brand brand-name"><span class="brand-name__mark"></span>Tern Holdings KR, LLC</div>

  <footer class="letterhead__footer">
    <div class="letterhead__notch"></div>
    <div class="letterhead__contacts">
      <span class="contact-item">
        <svg viewBox="0 0 10 10"><path d="M5 0a3.5 3.5 0 0 0-3.5 3.5C1.5 6 5 10 5 10s3.5-4 3.5-6.5A3.5 3.5 0 0 0 5 0zm0 5a1.5 1.5 0 1 1 0-3 1.5 1.5 0 0 1 0 3z"/></svg>
        4127 Orvell Ave. Suite 308, La Jolla CA 92037
      </span>
      <span class="contact-item">
        <svg viewBox="0 0 10 10"><path d="M0 2h10v6H0z M0 2l5 3 5-3" stroke="#333" stroke-width=".8"/></svg>
        wadehollins@mailvexa.example
      </span>
      <span class="contact-item">
        <svg viewBox="0 0 10 10"><circle cx="5" cy="5" r="4.5" fill="none" stroke="currentColor"/><path d="M.5 5h9M5 .5v9" stroke="currentColor" stroke-width=".8"/></svg>
        www.ternholdings.example
      </span>
    </div>
  </footer>
</section>

<section class="business-card">
  <div class="business-card__topbar"></div>
  <div class="business-card__panel"></div>
  <div class="business-card__tab"></div>
  <div class="business-card__brand brand-name"><span class="brand-name__mark"></span>Tern Holdings KR, LLC</div>
  <div class="business-card__name">Wade Hollins</div>

  <div class="business-card__details details--left">
    <div class="contact-item">
      <svg viewBox="0 0 10 10"><path d="M5 0a3.5 3.5 0 0 0-3.5 3.5C1.5 6 5 10 5 10s3.5-4 3.5-6.5A3.5 3.5 0 0 0 5 0z"/></svg>
      <span>4127 Orvell Ave. Suite 308,<br>La Jolla, CA 92037</span>
    </div>
    <div class="contact-item">
      <svg viewBox="0 0 10 10"><path d="M0 2h10v6H0z"/></svg>
      <span>wadehollins@mailvexa.example</span>
    </div>
  </div>

  <div class="business-card__details details--right">
    <div class="contact-item">
      <svg viewBox="0 0 10 10"><path d="M2 0l2 2.5-1 1.2c.7 1.4 1.9 2.6 3.3 3.3l1.2-1L10 8l-1.5 2C4 10 0 6 0 1.5z"/></svg>
      <span>555-283-7716</span>
    </div>
    <div class="contact-item">
      <svg viewBox="0 0 10 10"><circle cx="5" cy="5" r="4.5" fill="none" stroke="currentColor"/><path d="M.5 5h9M5 .5v9" stroke="currentColor" stroke-width=".8"/></svg>
      <span>www.ternholdings.example</span>
    </div>
  </div>
</section>

</body>
</html>
```